Kenwick Falcons FC Website

We are looking to develop a new website for Kenwick FC. Kenwick FC has now joined with Kenwick Falcons FC and we are looking at a website that can work for both clubs. Kenwick FC play in a local park football competition while kenwick Falcons are a Semi Professional team that plays in the Coastal Premier Division Competition. What we are after is two separate website off the one platform. I have attached both team logos for you to visualise. Also you can look at the existing kenwick website www.kenwickfc-demo.com.au. We are looking for a huge improvement in the website and it will be imperative we have links to sponsors and the sponsors can get regular visuals. Weare looking to move this club forward and have a very professional website that can communicate clearly with the community.

Hi All,

Please remember that the website is to represent two clubs;
1. Kenwick Falcons FC (Competes in Semi Professional League)
2. Kenwick FC (Compete in HBJCA League which is a lower level)

Further to this the Kenwick Falcons FC page will require a player profile page which will show photos of each player and a little bio on each.

Thanks

Reason: Would like to spend more time review existing and new designs

```html
<!DOCTYPE html>
<html lang="en">
<head>
<meta charset="utf-8">
<title>Kenwick FC</title>
<link rel="stylesheet" href="https://fonts.googleapis.com/css2?family=Open+Sans:wght@400;600;700&family=Roboto+Condensed:wght@400;700&family=Oswald:wght@400;500;700&display=swap">
<style>
:root{
  --red:#c4161c;
  --band-red:#b30f14;
  --dark-red:#8f0c10;
  --yellow:#f4c20d;
  --gold:#f5b21a;
  --ink:#1f1f1f;
  --grey:#555;
  --light:#eceef0;
  --footer:#262626;
  --footer-line:#3a3a3a;
  --footer-text:#b9b9b9;
  --white:#fff;
}
*{margin:0;padding:0;box-sizing:border-box}
html,body{width:1200px;height:2397px;overflow:hidden;background:var(--white)}
body{font-family:"Open Sans",Arial,sans-serif;color:var(--ink);position:relative}
section,header,footer{position:absolute;left:0;width:1200px}
.abs{position:absolute}

/* header */
.site-header{top:0;height:140px;z-index:3}
.brand{left:122px;top:34px;display:flex;align-items:center;gap:8px;color:var(--red);font-family:"Oswald",sans-serif;font-weight:700;font-size:20px;letter-spacing:.5px}
.brand-dot{width:20px;height:20px;border-radius:50%;background:var(--red)}
.main-nav{left:284px;top:38px;display:flex;gap:0;font-size:14px;font-family:"Open Sans",sans-serif}
.main-nav a{color:#222;text-decoration:none;text-transform:uppercase;margin-right:37px}
.main-nav a.active{color:var(--red)}

/* hero */
.hero{top:0;height:567px;clip-path:polygon(0 128px,1200px 80px,1200px 567px,0 567px)}
.hero-photo{position:absolute;inset:0;background:linear-gradient(180deg,#6f7f66 0%,#6d8f3e 30%,#4f8a2a 60%,#5d9a32 100%)}
.hero-title{left:560px;width:568px;top:296px;text-align:center;font-family:"Oswald",sans-serif;font-weight:500;font-size:60px;letter-spacing:3px;color:transparent;-webkit-text-stroke:2px var(--white)}
.hero-text{left:640px;width:410px;top:380px;text-align:center;color:#f2f2f2;font-size:14px;line-height:21px}
.btn-red{left:773px;top:459px;width:160px;height:38px;border-radius:19px;background:var(--red);border:2px solid #f1d6d6;color:var(--white);font-size:13px;display:flex;align-items:center;justify-content:center;text-transform:uppercase}
.hero-arrow{top:323px;width:54px;height:41px}
.hero-arrow.prev{left:0}
.hero-arrow.next{left:1127px;width:73px}

/* welcome band */
.welcome{top:567px;height:331px;background:var(--band-red)}
.welcome-title{left:120px;top:60px;width:330px;font-family:"Oswald",sans-serif;font-weight:500;font-size:44px;line-height:42px;letter-spacing:2px;color:transparent;-webkit-text-stroke:1.6px var(--gold);text-align:center}
.season{left:120px;width:320px;top:178px;text-align:center;color:var(--white);font-size:18px;font-weight:600;letter-spacing:.5px}
.btn-register{left:125px;top:210px;width:302px;height:52px;border-radius:26px;background:linear-gradient(180deg,#ffd84a,#f1b50c);border:2px solid #ffe98e;display:flex;align-items:center}
.btn-register .ball{width:40px;height:40px;margin-left:4px}
.btn-register span{margin-left:28px;font-family:"Oswald",sans-serif;font-weight:500;font-size:24px;color:#222;letter-spacing:1px}
.talk-title{left:481px;top:64px;font-family:"Oswald",sans-serif;font-weight:500;font-size:28px;letter-spacing:2px;color:transparent;-webkit-text-stroke:1.2px #f3dede}
.talk-rule{left:481px;top:120px;width:600px;height:1px;background:rgba(255,255,255,.35)}
.talk-lead{left:484px;top:136px;width:600px;color:var(--white);font-size:14px;line-height:22px}
.talk-body{left:484px;top:195px;width:600px;color:#f4d8d8;font-size:12px;line-height:20px}

/* fixtures */
.fixtures{top:898px;height:644px;background:linear-gradient(180deg,#dfe3e6 0%,#eef0f2 40%,#fbfbfb 100%)}
.section-title{width:1200px;text-align:center;top:82px;font-family:"Oswald",sans-serif;font-weight:500;font-size:36px;letter-spacing:2px;color:transparent;-webkit-text-stroke:1.4px var(--red)}
.fixtures-intro{left:136px;width:930px;top:134px;text-align:center;font-size:14px;line-height:22px;color:#333}
.fixtures-rule{left:136px;top:204px;width:931px;height:1px;background:#cfd2d5}
.fixture-col{top:262px;list-style:none;font-family:"Roboto Condensed",sans-serif;font-weight:700;font-size:18px;color:#222;text-transform:uppercase}
.fixture-col li{height:34px;display:flex;align-items:center;gap:14px}
.fixture-col li svg{width:12px;height:12px;flex:none}
.col-1{left:146px}.col-2{left:540px}.col-3{left:876px}
.col-divider{top:245px;width:1px;height:359px;background:#c9c9c9}

/* no smoking */
.no-smoking{top:1542px;height:245px;background:linear-gradient(180deg,#e4e4e4,#f3f3f3 50%,#dcdcdc)}
.ns-title{left:120px;top:62px;display:flex;align-items:center;gap:12px;font-family:"Oswald",sans-serif;font-weight:400;font-size:46px;letter-spacing:1px;color:#444}
.ns-title em{font-style:normal;color:var(--red)}
.ns-text{left:121px;top:128px;font-size:20px;color:#444}
.btn-yellow{left:120px;top:160px;width:112px;height:26px;border-radius:13px;background:var(--yellow);border:2px solid #ffe9a0;font-size:9px;display:flex;align-items:center;justify-content:center;color:#333;text-transform:uppercase}
.ashtray{left:527px;top:0;width:592px;height:245px;background:radial-gradient(ellipse at 55% 55%,#ffffff 0%,#f2f2f2 35%,#dedede 70%,transparent 100%)}

/* sponsors */
.sponsors{top:1787px;height:231px;background:var(--white)}
.ribbon{left:499px;top:44px;width:204px;height:42px}
.carousel-btn{top:118px;width:26px;height:73px;display:flex;align-items:center;justify-content:center}
.carousel-btn.prev{left:115px;background:#e3e3e3}
.carousel-btn.next{left:1066px;background:var(--red)}
.sponsor{top:118px;height:73px;border:1px solid #dcdcdc;background:var(--white);display:flex;align-items:center;justify-content:center;font-size:13px;font-weight:700;color:#333;text-align:center;padding:0 6px}

/* footer */
.site-footer{top:2018px;height:379px;background:var(--footer);color:var(--footer-text)}
.foot-title{top:62px;font-size:15px;color:#d92026;text-transform:uppercase}
.foot-rule{top:90px;height:1px;background:var(--footer-line)}
.sitemap{left:120px;top:112px;list-style:none;font-size:13px}
.sitemap li{height:28px;display:flex;align-items:center;gap:12px}
.sitemap li::before{content:"";width:6px;height:6px;border:1px solid #8a8a8a}
.sitemap li.current{color:var(--yellow)}
.sitemap li.current::before{border-color:var(--yellow)}
.news-item{left:393px;width:330px;height:48px;display:flex;gap:10px}
.news-thumb{width:66px;height:45px;flex:none;background:linear-gradient(135deg,#8d8d8d,#4b4b4b)}
.news-item p{font-size:11px;line-height:14px;color:#d5d5d5;font-weight:600}
.news-item small{display:block;font-size:9px;color:#8a8a8a;font-style:italic;font-weight:400;margin-top:2px}
.news-nav{top:62px;width:16px;height:16px;border-radius:50%}
.view-all{left:1018px;top:62px;width:61px;height:16px;border-radius:8px;background:var(--yellow);color:#222;font-size:9px;display:flex;align-items:center;justify-content:center;text-transform:uppercase}
.gallery{left:796px;top:115px;width:283px;height:181px;display:grid;grid-template-columns:repeat(3,1fr);grid-template-rows:repeat(3,1fr);gap:3px}
.gallery div{background:#7a4a44}
.bottom-rule{left:120px;top:325px;width:960px;height:1px;background:var(--footer-line)}
.copyright{left:120px;top:346px;font-size:10px;color:#8a8a8a}
.social{left:916px;top:340px;display:flex;gap:5px}
.social span{width:26px;height:26px;border-radius:50%;border:1.5px solid #777}
.social span.on{border-color:#3aa3e3}
</style>
</head>
<body>

<section class="hero">
  <div class="hero-photo" role="img" aria-label="Photo of a youth footballer dribbling the ball on a grass pitch with spectators behind"></div>
  <div class="abs hero-title">KENWICK FC</div>
  <p class="abs hero-text">Lorem Ipsum is simply dummy text of the printing and typesetting industry. Lorem Ipsum has been the industry's standard dummy text .</p>
  <div class="abs btn-red">Find out more</div>
  <svg class="abs hero-arrow prev" viewBox="0 0 54 41" aria-label="Previous slide"><path d="M0 0H34A20.5 20.5 0 0 1 34 41H0Z" fill="#fff"/><circle cx="33" cy="20.5" r="14" fill="#222"/><path d="M36 13L28 20.5 36 28" stroke="#fff" stroke-width="3.5" fill="none"/></svg>
  <svg class="abs hero-arrow next" viewBox="0 0 73 41" aria-label="Next slide"><path d="M73 0H20A20.5 20.5 0 0 0 20 41H73Z" fill="#c4161c"/><circle cx="21" cy="20.5" r="14" fill="#222"/><path d="M18 13L26 20.5 18 28" stroke="#c4161c" stroke-width="3.5" fill="none"/></svg>
</section>

<header class="site-header">
  <svg class="abs" style="left:0;top:0" width="1200" height="130" aria-hidden="true"><polygon points="0,0 1200,0 1200,80 0,128" fill="#fff"/></svg>
  <div class="abs brand"><span class="brand-dot"></span>KENWICK FC</div>
  <nav class="abs main-nav">
    <a class="active" href="#">Home</a><a href="#">About us</a><a href="#">News</a><a href="#">Fixture &amp; Results</a><a href="#">Photo Gallery</a><a href="#">Sponsor</a><a href="#">Club</a><a href="#">Contact us</a>
  </nav>
</header>

<section class="welcome">
  <h1 class="abs welcome-title">WELCOME TO<br>KENWICK FC</h1>
  <div class="abs season">2014 SEASON</div>
  <div class="abs btn-register">
    <svg class="ball" viewBox="0 0 40 40"><circle cx="20" cy="20" r="19" fill="#222"/><circle cx="20" cy="20" r="12" fill="#fff"/><polygon points="20,14 26,18 24,25 16,25 14,18" fill="#222"/></svg>
    <span>REGISTER ONLINE</span>
  </div>
  <h2 class="abs talk-title">LET'S TALK ABOUT KENWICK FC.</h2>
  <div class="abs talk-rule"></div>
  <p class="abs talk-lead">Lorem Ipsum is simply dummy text of the printing and typesetting industry. Lorem Ipsum has been the industry's standard</p>
  <p class="abs talk-body">Dummy text ever since the 1500s, when an unknown printer took a galley of type and scrambled it to make a type specimen book. It has survived not only five centuries, but also the leap into electronic typesetting, remaining essentially unchanged.</p>
</section>

<section class="fixtures">
  <h2 class="abs section-title">FIXTURES &amp; RESULTS</h2>
  <p class="abs fixtures-intro">Lorem Ipsum is simply dummy text of the printing and typesetting industry. Lorem Ipsum has been the industry's standard dummy text ever since the 1500s, when an unknown printer took a galley of type and scrambled it to make a type specimen book.</p>
  <div class="abs fixtures-rule"></div>
  <svg width="0" height="0" style="position:absolute"><defs><symbol id="ball" viewBox="0 0 12 12"><circle cx="6" cy="6" r="5.5" fill="#fff" stroke="#333"/><polygon points="6,3.6 8.2,5.2 7.4,7.8 4.6,7.8 3.8,5.2" fill="#333"/></symbol></defs></svg>
  <ul class="abs fixture-col col-1">
    <li><svg><use href="#ball"/></svg>Premier League</li>
    <li><svg><use href="#ball"/></svg>Premier League Res</li>
    <li><svg><use href="#ball"/></svg>Super League</li>
    <li><svg><use href="#ball"/></svg>Super League Res</li>
    <li><svg><use href="#ball"/></svg>Under 16 / 2</li>
    <li><svg><use href="#ball"/></svg>Under 17 / 1</li>
    <li><svg><use href="#ball"/></svg>Under 10 / 2</li>
    <li><svg><use href="#ball"/></svg>Under 10 / 3</li>
    <li><svg><use href="#ball"/></svg>Under 11 / 1</li>
    <li><svg><use href="#ball"/></svg>Under 12 / 3</li>
  </ul>
  <div class="abs col-divider" style="left:435px"></div>
  <ul class="abs fixture-col col-2">
    <li><svg><use href="#ball"/></svg>Under 13 / 3</li>
    <li><svg><use href="#ball"/></svg>Under 14 / 3</li>
    <li><svg><use href="#ball"/></svg>AA Men / 5</li>
    <li><svg><use href="#ball"/></svg>AA Men / 6</li>
    <li><svg><use href="#ball"/></svg>AA Men / 8</li>
    <li><svg><use href="#ball"/></svg>AA Men / 10</li>
    <li><svg><use href="#ball"/></svg>AA Men / 10</li>
    <li><svg><use href="#ball"/></svg>AA Men / 14</li>
    <li><svg><use href="#ball"/></svg>07 ECL / Red</li>
    <li><svg><use href="#ball"/></svg>07 ECL / Green</li>
  </ul>
  <div class="abs col-divider" style="left:770px"></div>
  <ul class="abs fixture-col col-3">
    <li><svg><use href="#ball"/></svg>07 ECL / Blue</li>
    <li><svg><use href="#ball"/></svg>08 ECL / Blue</li>
    <li><svg><use href="#ball"/></svg>08 ECL / Green</li>
    <li><svg><use href="#ball"/></svg>09 / Green</li>
    <li><svg><use href="#ball"/></svg>06 / A Green</li>
    <li><svg><use href="#ball"/></svg>06 / B Blue</li>
    <li><svg><use href="#ball"/></svg>06 / C Red</li>
    <li><svg><use href="#ball"/></svg>06 / D Purple</li>
    <li><svg><use href="#ball"/></svg>06 / E White</li>
    <li><svg><use href="#ball"/></svg>06 / F Brown</li>
  </ul>
</section>

<section class="no-smoking">
  <div class="abs ashtray" role="img" aria-label="Photo of a white ashtray surrounded by scattered cigarette butts and ash"></div>
  <div class="abs ns-title">
    <svg width="38" height="38" viewBox="0 0 38 38"><circle cx="19" cy="19" r="16" fill="none" stroke="#c4161c" stroke-width="3.5"/><rect x="9" y="17" width="20" height="5" fill="#c4161c"/><line x1="8" y1="8" x2="30" y2="30" stroke="#c4161c" stroke-width="3.5"/></svg>
    <span>NO <em>SMOKING</em></span>
  </div>
  <p class="abs ns-text">There is a No Smoking Ban for all Sports Grounds</p>
  <div class="abs btn-yellow">Find out more</div>
</section>

<section class="sponsors">
  <svg class="abs ribbon" viewBox="0 0 204 42"><polygon points="12,0 192,0 204,21 192,42 12,42 0,21" fill="#c4161c"/><text x="102" y="28" text-anchor="middle" fill="#fff" font-family="Open Sans, sans-serif" font-size="19">OUR SPONSORS</text></svg>
  <div class="abs carousel-btn prev"><svg width="12" height="22"><path d="M10 2L2 11 10 20" stroke="#fff" stroke-width="2.5" fill="none"/></svg></div>
  <div class="abs sponsor" style="left:150px;width:163px">Bright Tide Media</div>
  <div class="abs sponsor" style="left:326px;width:128px">Kestrel</div>
  <div class="abs sponsor" style="left:467px;width:147px">Northvale</div>
  <div class="abs sponsor" style="left:620px;width:169px">Harlow Pereira &amp; Co</div>
  <div class="abs sponsor" style="left:797px;width:147px">Ironleaf Seal</div>
  <div class="abs sponsor" style="left:954px;width:102px;font-size:11px">Kenwick Bowling Club</div>
  <div class="abs carousel-btn next"><svg width="12" height="22"><path d="M2 2L10 11 2 20" stroke="#fff" stroke-width="2.5" fill="none"/></svg></div>
</section>

<footer class="site-footer">
  <h3 class="abs foot-title" style="left:120px">Site Map</h3>
  <div class="abs foot-rule" style="left:120px;width:200px"></div>
  <ul class="abs sitemap">
    <li>Become A Referee</li><li>News</li><li>Fixture &amp; Results</li><li class="current">Photo Gallery</li><li>Sponsor</li><li>Club</li><li>Contact Us</li>
  </ul>

  <h3 class="abs foot-title" style="left:392px">Latest News</h3>
  <span class="abs news-nav" style="left:675px;background:#666"></span>
  <span class="abs news-nav" style="left:697px;background:var(--yellow)"></span>
  <div class="abs foot-rule" style="left:392px;width:332px"></div>
  <div class="abs news-item" style="top:118px"><div class="news-thumb" role="img" aria-label="News photo of a football match"></div><p>Lorem Ipsum is simply dummy text of the typesetting industry.<small>Mar 11, 2014</small></p></div>
  <div class="abs news-item" style="top:181px"><div class="news-thumb" role="img" aria-label="News photo of a player in action"></div><p>Lorem Ipsum is simply dummy text of the typesetting industry.<small>Mar 11, 2014</small></p></div>
  <div class="abs news-item" style="top:244px"><div class="news-thumb" role="img" aria-label="News photo of a player on the ball"></div><p>Lorem Ipsum is simply dummy text of the typesetting industry.<small>Mar 11, 2014</small></p></div>

  <h3 class="abs foot-title" style="left:794px">Photo Gallery</h3>
  <div class="abs view-all">View all</div>
  <div class="abs foot-rule" style="left:794px;width:285px"></div>
  <div class="abs gallery" role="img" aria-label="Grid of club photos: players, team groups and match moments">
    <div style="background:#b8423a"></div><div style="background:#6d5a4c"></div><div style="background:#5e5046"></div>
    <div style="background:#a53a33"></div><div style="background:#c8c3bd"></div><div style="background:#4e5f3e"></div>
    <div style="background:#7e5a50"></div><div style="background:#9c6b5e"></div><div style="background:#b34a42"></div>
  </div>

  <div class="abs bottom-rule"></div>
  <p class="abs copyright">Copyright .KENWICK FC © 2014. All rights reserved. Terms and Conditions</p>
  <div class="abs social" aria-label="Social links"><span class="on"></span><span></span><span></span><span></span><span></span></div>
</footer>

</body>
</html>
```